The Ballad of Orlena

I need a design for a two-page spread to open a very long (and fascinating) story about a famous female architect who basically built our very charming village. I've enclosed copy, photo of her, and several images of key buildings.

My present concept (I'm very open to other ideas) is a female hand with a drafting pencil, working on a blue line, with our town's iconic buildings designed by Orlena Pratt, Ojai, California, gradually coming into view toward the bottom of the page.

The first paragraph of copy (above the byline) should go on the first left-hand page, then the 7,500 story should follow on the right-hand side. But again, just a suggestion.

Our quarterly magazine is universally regarded as having superior, long-form journalism (the Harbor Quill of California, as someo, but our design execution is weak. We need your help.

Target Market(s)

Ojai is an affluent, highly artistic community. And our magazine is expanding nationwide to appeal to both tourists and the rising creative class of people who would be drawn to a community like Ojai.

Industry/Entity Type

Architect

Requirements
Must have
• Page specs …

8.375" by 10.875" trim
8.875" by 11.375" bleed (.25" all around)
Spread 17.25" by 11.375" bleed.

Copy …
We use Neutra for headlines and cutlines, Berkeley OldStyle for copy, subheads. But I like the idea of using Glimmerset - the old Quest of Morvane typeface for the main headline.

```html
<!DOCTYPE html>
<html lang="en">
<head>
<meta charset="utf-8">
<title>The Ballad of Orlena</title>
<link rel="stylesheet" href="https://fonts.googleapis.com/css2?family=Cinzel:wght@400;700&family=Josefin+Sans:wght@400;700&family=Sorts+Mill+Goudy&display=swap">
<style>
:root{
  --paper:#ffffff;
  --ink:#231f20;
  --title-red:#c3202b;
  --night:#050505;
  --sky:#dfe6ee;
  --photo-dark:#3a3633;
  --photo-light:#b9b3ac;
}
*{box-sizing:border-box;margin:0;padding:0}
html,body{width:1200px;height:923px;overflow:hidden;background:var(--paper)}
.spread{position:relative;width:1200px;height:923px;color:var(--ink);
  font-family:"Sorts Mill Goudy",Georgia,serif;font-size:13.4px;line-height:19.2px}
.column{position:absolute;text-align:justify;hyphens:auto;overflow:hidden}
.column p{text-indent:18px}
.column p.flush{text-indent:0}
.col-left{left:18px;top:6px;width:381px;height:912px}
.col-a{left:405px;top:452px;width:188px;height:463px}
.col-b{left:603px;top:452px;width:188px;height:463px}
.col-c{left:800px;top:2px;width:188px;height:913px}
.col-d{left:998px;top:2px;width:190px;height:913px}
.intro::first-letter{float:left;font-size:66px;line-height:52px;margin:4px 4px 0 0;color:var(--ink)}
.intro{text-indent:0!important}
.feature-title{font-family:"Josefin Sans",sans-serif;font-weight:700;font-size:31px;
  letter-spacing:1px;line-height:36px;margin:40px 0 4px}
.byline{text-indent:0!important;margin-bottom:10px}
.editor-note{text-transform:uppercase}
.portrait{float:right;width:190px;margin:8px 33px 6px 10px;text-indent:0}
.portrait .photo{display:block;width:190px;height:283px;
  background:radial-gradient(ellipse at 50% 38%,var(--photo-light) 0,#857e77 35%,var(--photo-dark) 75%)}
.portrait .cutline{display:block;font-family:"Josefin Sans",sans-serif;font-weight:700;
  font-size:13px;letter-spacing:.5px;text-align:center;margin-top:4px;line-height:16px}
.subhead{font-family:"Josefin Sans",sans-serif;font-weight:400;font-size:25px;
  line-height:26px;letter-spacing:.5px;text-transform:uppercase;text-align:justify;
  text-align-last:justify;margin:6px 0 8px}
.opener{position:absolute;left:403px;top:0;width:388px;height:447px;overflow:hidden}
.opener .art{position:absolute;inset:0;
  background:
   linear-gradient(180deg,transparent 0,transparent 72%,#b9a98e 78%,#d8c9ad 84%,#6d6a58 93%,#3b3a33 100%),
   linear-gradient(180deg,var(--night) 0,var(--night) 30%,#5b6470 42%,var(--sky) 56%,#f4f6f8 68%,#eef1f4 100%)}
.opener .kicker,.opener .name{position:absolute;left:0;width:100%;text-align:center;
  font-family:"Cinzel",serif;color:var(--title-red)}
.opener .kicker{top:30px;font-size:29px;letter-spacing:1px;padding-left:40px}
.opener .name{top:56px;font-size:84px;font-weight:700;letter-spacing:-1px;line-height:100px}
.folio{position:absolute;right:12px;bottom:6px;display:flex;align-items:center;gap:6px;
  font-family:"Josefin Sans",sans-serif;font-weight:700;font-size:22px}
</style>
</head>
<body>
<div class="spread">

  <section class="column col-left">
    <p class="intro">Ojai didn't take its present form through gradual changes. Instead, it was through several phases of what biologists call “punctuated equilibrium.” First, the fire of 1916 left a clean slate for Edmund Marsh Lindley and his merry band of civic pioneers and philanthropists. Then, the Hollywood Blacklist brought Ojai another. Her name was Orlena Pratt. This is her story.</p>
    <h2 class="feature-title">ORLENA'S WORLD</h2>
    <p class="byline">By Eleanor Hayes Whitcomb</p>
    <p class="flush">Few individuals have left so many indelible marks on the Ojai area landscape as architect Orlena Pratt, a supreme talent, a great wit and a dear friend. She and I became acquainted through our mutual support of Ventura County Supervisor Margaret Olsen Tolliver. Orlena, “citizen warrior” Celia Brandt, Doris Feldman — county Counsel for Ventura County, the first woman in the state to hold such a position (<span class="editor-note">this seems out of place in a story about Orlena Pratt</span>)— <span class="portrait"><span class="photo" role="img" aria-label="Black and white portrait of architect Orlena Pratt"></span><span class="cutline">ORLENA PRATT</span></span>and I would travel from Ojai to wherever the “Friends of Margaret” were meeting and, in the process, became great friends.</p>
    <p>Before long, we became “Ladies Who Lunch,” whenever we could work it into our schedules. It was in 1993, when Orlena, Vice President (Vice Chair? Don't think commission has VP, but you'd know better than I) of the Ojai Historic Preservation Commission, suggested I join her on the commission — not because I knew anything about history, preservation, or city law, but because she said she would have much more fun with me on board. Now, for the rest of her story.</p>
    <p>Orlena's creations in Ojai are lived in, learned in, worked in, prayed in and crossed over. But I didn't realize how little I knew about Orlena until after her death in 1996, when I was asked to give a talk about her life; research led me to discover her roots, her childhood, her marriage to the equally talented Julian Pratt — and her fabulous career.</p>
    <p class="editor-note">We could use more description about Orlena's work and its meaning to Ojai before launching into the old country.</p>
    <p>Consider, for example, the story of her parents and the precarious life they lived in Lithuania and Belarus. Simna, Lithuania, the home of Orlena's mother, Hannah Lebedovsky,</p>
  </section>

  <figure class="opener">
    <div class="art" role="img" aria-label="Blueprint-style illustration of a hand drawing with a drafting pencil, fading down into photographs of Ojai's arcade and a modern civic building"></div>
    <div class="kicker">THE BALLAD OF</div>
    <h1 class="name">ORLENA</h1>
  </figure>

  <section class="column col-a">
    <p class="flush">was about two hours out of Vilnius — since the 14th century, the center of Jewish culture and learning. But by the time of Hannah's birth in 1892, Lithuanians had been forbidden to speak their own language and Jews were forbidden to own land, reduced to living in ghettos and subject to periodic pogroms of Czarist Russia. Hannah, orphaned at an early age, was living with her Tante Feyga.</p>
    <p>About 200 miles away, in Belarus, the same sort of persecution was underway, a period of intense “Russification.” Orlena's father, Hirsch Halpern, who was living with his widowed mother and apprenticed to a hat-maker, was stopped by</p>
  </section>

  <section class="column col-b">
    <p class="flush">the police on one of his deliveries. A note was discovered in he hat: “Come to meeting tonight.” With that startling discovery, as well as the threat of enforced service in the Czar's Army, Hirsch and his mother decided it was time for him to leave for the land of opportunity. He was 16 years of age.</p>
    <p>On the way, he and a cousin stopped in to visit friends and relatives in Simna. Hannah was entranced. Many years later, she would relate: “I thought he was the smartest and loveliest looking person I'd ever seen.” But, at 11 years of age, she was far too young to think of joining him on his adventure, said Tante Feyga.</p>
    <p>But just one-and-a-half</p>
  </section>

  <section class="column col-c">
    <p class="flush">years later, bearing a goose-down quilt, a long bread and long salami as dowry, 12-almost-13-years-old Hannah set out for New York City to join relatives who had emigrated earlier. After her arrival, she was cautioned by Tante Bluma, “You cannot go chasing after a boy without observing the proprieties; you simply must have a hat.”</p>
    <p>So Hannah submitted an ad to the Metropolitan Ledger: “Excellent seamstress recently arrived NYC. Wishes employment.” In short order, Hannah had a job, purchased her hat, found her beau, and was married at a very young age.</p>
    <p>Both Hannah and Hirsch would have passed through Ellis Island at this time in the emigration process into New York City. Thanks mostly to the assistance of the immigration officers, and other American helpers, Hannah Lebedovsky became Ruth Lane just as Hirsch Halpern became Harold or “Harry” Halpern. Soon thereafter, she became Ruth Halpern.</p>
    <p>Their first child, Miriam Halpern, was born October 2, 1915; Orlena, November 23, 1918. The family was secure, but Ruth hated the sweatshops of New York City; Harold hated New York City itself.</p>
    <h3 class="subhead">The West of the Story</h3>
    <p>One of Harry's friends had opened a dry goods store in Texas. “If you really want to leave New York,” he wrote, “Come to El Paso. I'll give you a couple of bolts of cloth</p>
  </section>

  <section class="column col-d">
    <p class="flush">and we can find a car for you. You can open your own business.” Harry made it to Texas, acquired his bolts of cloth, a Kestrel roadster, found a good spot, and sent for the family who arrived by train to Miami, Arizona.</p>
    <p>Miami was the typical classic western copper-boom town. Where Harry saw possibilities,</p>
    <p>Ruth saw hills with no vegetation, scarred by copper and silver mining, a town with no center – hard drinking, rough characters, definitely not a place she'd like to raise her daughters.</p>
    <p>The family stayed for two years, regrouping, but then set off to join Harry's sister in Los Angeles and continue looking for that elusive perfect spot. As the family left the tawny, parched hills of Arizona, and entered the Mojave Desert, they almost lost heart.</p>
    <p>But things improved as they entered California proper, so to speak. Harry left the family with his sister, and set out again in his roadster, returning within the week. “I've found it, he said, “the prettiest little town I've ever seen, between two sets of hills with orange trees growing in the valley and oil being pumped on the hills.” Had Harold only known: There was a serpent in his paradise; Santa Paula was the one place in Ventura County where the Ku Klux Klan flourished. As advertised in the Ventura Evening Herald, July 31, 1923: “The Klan is an organization for all native-born white</p>
  </section>

  <div class="folio">
    <svg width="30" height="16" viewBox="0 0 30 16" aria-hidden="true">
      <path d="M1 8h24M18 2l7 6-7 6" fill="none" stroke="#231f20" stroke-width="2.2" stroke-linecap="round" stroke-linejoin="round"/>
    </svg>
    <span>P.23</span>
  </div>
</div>
</body>
</html>
```